[Design ONLY] Design for our Ecommerce business website

We require a web design for our ecommerce business website. We sell textbooks, Computer & Accessories, Gifts and stationery and Laptop/IT support service etc
Requirement:
We Require 3 pages for each design: Homepage, Product page and Payment page
Design Approach:
Design UI to be have a modern and professional feel and user experience must be good.
Responsive web design approach.
1. Home page
- Logo/Heading
- Navigation links to other pages eg. About us
- Appropriate images/banners
- A special offer
- Recent News
Include an overview of the business:
- provide general information
- contact information
- links to social media
- Frequently Asked Questions (FAQ) page
Publish store policies and make sure they are not too difficult to find:
- shipping and return policies
- outline the return process and what products can be returned
- provide easy access to a privacy policy that covers shoppers’ personal and financial information (this is crucial)
2. Product
Product Pages should include:
- Pictures, descriptions, order and price information for your products and/or services.
- Navigation links to other pages, especially home, about us, order and other product pages.
- Links to a shopping cart
- Add to wishlist
- Related or recommend products
3. Payment
- Standard payment form with payment integration with Brenox and Lumbix.
- Shipping or Self Collection fee
User Experience Aspect:
Well-Defined Product Categories
a. The top level of navigation should show the set of categories that the site offers. Group products into categories and subcategories. Category labels work best as single words that describe the range of products, so shoppers can scan through them and instantly understand what they represent.
Product Search
a. Build a search function that helps them easily find what they are looking for.
Make search omnipresent: Put the search box on every page and in familiar locations. The box should be visible, quickly recognizable, and easy to use.
b. Allow sorting and filtering of results: Let shoppers sort search results based on various criteria (best sellers, highest or lowest price, product rating, newest item, etc.) as well as eliminate items that do not fit within a certain category.
Product Quick view
a. A “quick view” reduces the time it takes for shoppers to find the right product by eliminating unnecessary page loads. Also, be sure to include a prominently positioned “Add to Cart” button as well as a “Save to Wishlist” functionality.
b. Show Related and Recommended Products. This can be displayed on a product detail page.
Target Market(s)
university students
Number of Pages Required
3 page
Requirements
Must have
- Note * its a university store. not a normal ecommerce shop*
Do include design for the 3 pages specified. Homepage, product page and payment page.

```html
<!DOCTYPE html>
<html lang="en">
<head>
<meta charset="utf-8">
<title>Uni Store Gifts – Home</title>
<link href="https://fonts.googleapis.com/css2?family=Montserrat:wght@400;500;600;700;800&family=Playfair+Display:wght@700&display=swap" rel="stylesheet">
<style>
:root{
  --accent:#e9505a;
  --navy:#1d2a4d;
  --ink:#2b2b2b;
  --muted:#8a8a8a;
  --line:#e4e4e4;
  --soft:#f3f3f3;
  --star:#f2b01e;
  --white:#ffffff;
}
*{margin:0;padding:0;box-sizing:border-box}
html,body{width:1200px;height:3448px;overflow:hidden;background:var(--white)}
body{position:relative;font-family:'Montserrat',sans-serif;color:var(--ink)}
.abs{position:absolute}
.img{position:absolute;display:block}

/* header */
.search-icon{left:116px;top:30px}
.logo{left:560px;top:10px;width:80px;text-align:center;font-weight:800;color:var(--navy);font-size:30px;line-height:28px;letter-spacing:1px}
.logo small{display:block;font-size:13px;line-height:14px;font-weight:700;letter-spacing:3px}
.account{left:930px;top:22px;display:flex;align-items:center;gap:8px;white-space:nowrap}
.account .txt{font-size:10px;line-height:13px;font-weight:700;color:var(--navy)}
.account .txt span{display:block;font-weight:500;color:var(--muted);font-size:8px}
.hdr-icons{left:1044px;top:24px;display:flex;gap:14px;align-items:center}
.nav{left:0;top:80px;width:1200px;display:flex;justify-content:center;gap:30px;border-top:1px solid var(--line);border-bottom:1px solid var(--line);height:36px;align-items:center}
.nav a{font-size:10px;font-weight:600;color:var(--ink);text-decoration:none;letter-spacing:.5px;padding:5px 10px}
.nav a.active{border:1px solid var(--ink)}

/* hero */
.hero{left:0;top:120px;width:1200px;height:460px;background:linear-gradient(100deg,#3c3632 0%,#6d6259 45%,#8b8079 70%,#514842 100%)}
.hero-box{left:120px;top:280px}
.hero-box .pre{display:inline-block;border:2px solid var(--white);padding:6px 12px;color:var(--white);font-size:14px;font-weight:600;letter-spacing:1px}
.hero-box h1{color:var(--accent);font-size:40px;font-weight:800;letter-spacing:1px;margin-top:4px}
.hero-box .sub{color:var(--white);font-size:22px;font-weight:600}
.btn-red{display:inline-block;background:var(--accent);color:var(--white);font-size:11px;font-weight:600;padding:6px 12px;margin-top:14px}

/* sections */
.title{left:0;width:1200px;text-align:center;font-family:'Playfair Display',serif;font-size:20px;font-weight:700;color:var(--ink)}
.row{left:132px;width:936px;display:flex;gap:20px}
.card{width:219px}
.card .pic{height:232px;position:relative}
.card .cap{text-align:center;font-size:15px;font-weight:500;margin-top:20px}
.card .name{font-size:15px;font-weight:500;margin-top:22px}
.card .meta{display:flex;justify-content:space-between;margin-top:8px;font-size:11px;color:var(--muted)}
.stars{color:var(--star);letter-spacing:1px;font-size:12px}
.arrow{position:absolute;color:var(--muted);font-size:22px}
.quick{position:absolute;left:50%;top:50%;transform:translate(-50%,-50%);background:var(--navy);color:var(--white);font-size:10px;font-weight:700;padding:8px 14px;letter-spacing:.5px;white-space:nowrap}

/* banners */
.banner{left:0;top:972px;width:1200px;height:348px;background:linear-gradient(90deg,#c9c2b6 0%,#b19a7f 40%,#d2cbc2 70%,#b33d3f 100%)}
.banner-box{left:660px;top:1100px;width:400px;background:rgba(110,100,95,.72);padding:14px 20px}
.banner-box h3{color:var(--white);font-size:22px;font-weight:700;letter-spacing:1px}
.banner-box .b2{color:var(--white);font-size:14px;font-weight:700;letter-spacing:.5px}
.banner-box p{color:#eee;font-size:10px}
.promo{top:1780px;width:472px;height:240px}
.promo .inner{position:absolute;left:30px;top:70px}
.promo h3{color:var(--white);font-size:38px;font-weight:600}
.promo p{color:#f1f1f1;font-size:10px;margin-top:4px;width:220px}
.btn-navy{display:inline-block;background:var(--navy);color:var(--white);font-size:11px;font-weight:600;padding:7px 14px;margin-top:14px}

/* history */
.history{left:200px;top:2448px;width:800px;text-align:center}
.history h2{font-size:15px;font-weight:700;letter-spacing:1px}
.history .lead{color:var(--accent);font-size:11px;margin-top:14px}
.history p{font-size:10px;line-height:17px;color:var(--muted);margin-top:16px}
.btn-outline{display:inline-block;border:1px solid var(--accent);color:var(--accent);font-size:10px;padding:7px 16px;margin-top:30px;letter-spacing:.5px}

/* photofeed */
.feed{left:0;top:2800px;width:1200px;height:200px;background:var(--soft)}
.feed-title{left:0;top:2856px;width:1200px;text-align:center;font-size:13px;font-weight:600}
.feed-row{left:240px;top:2888px;display:flex;gap:4px}
.feed-row div{width:116px;height:88px}

/* newsletter */
.news{left:240px;top:3020px;width:720px;height:152px;border:1px solid var(--line);text-align:center;padding-top:20px}
.news h2{font-family:'Playfair Display',serif;color:var(--accent);font-size:28px;letter-spacing:1px}
.news p{font-size:9px;color:var(--muted);margin-top:6px}
.news .form{display:flex;justify-content:center;margin-top:14px}
.news .field{width:280px;height:30px;border:1px solid var(--line);font-size:9px;color:var(--muted);text-align:left;padding:10px}
.news .sub-btn{background:var(--navy);color:var(--white);font-size:10px;font-weight:700;padding:9px 16px}

/* footer */
.foot{top:3200px;width:220px}
.foot h4{color:var(--accent);font-size:12px;font-weight:700;margin-bottom:12px;letter-spacing:.5px}
.foot li{list-style:none;font-size:10px;color:var(--muted);line-height:18px;display:flex;align-items:center;gap:8px}
.dot{width:10px;height:10px;border-radius:50%;background:var(--accent)}
.copy{left:0;top:3422px;width:1200px;text-align:center;font-size:9px;color:var(--muted);border-top:1px solid var(--line);padding-top:8px}
</style>
</head>
<body>

<!-- header -->
<svg class="abs search-icon" width="16" height="16" viewBox="0 0 16 16"><circle cx="6.5" cy="6.5" r="5" fill="none" stroke="#2b2b2b" stroke-width="1.6"/><line x1="10.2" y1="10.2" x2="15" y2="15" stroke="#2b2b2b" stroke-width="1.8"/></svg>
<div class="abs logo">UNI<small>STORE</small></div>
<div class="abs account">
  <svg width="16" height="16" viewBox="0 0 16 16"><circle cx="8" cy="5" r="3.2" fill="none" stroke="#1d2a4d" stroke-width="1.5"/><path d="M2 15c0-3.5 2.7-5.5 6-5.5s6 2 6 5.5" fill="none" stroke="#1d2a4d" stroke-width="1.5"/></svg>
  <div class="txt">WELCOME TO<span>LOGIN &amp; REGISTER</span></div>
</div>
<div class="abs hdr-icons">
  <svg width="18" height="16" viewBox="0 0 18 16"><path d="M9 15S1 10 1 5a4 4 0 0 1 8-1 4 4 0 0 1 8 1c0 5-8 10-8 10z" fill="none" stroke="#2b2b2b" stroke-width="1.5"/></svg>
  <svg width="18" height="18" viewBox="0 0 18 18"><path d="M1 2h3l2 10h9l2-7H5" fill="none" stroke="#2b2b2b" stroke-width="1.5"/><circle cx="7" cy="15.5" r="1.4" fill="#2b2b2b"/><circle cx="14" cy="15.5" r="1.4" fill="#2b2b2b"/></svg>
</div>
<nav class="abs nav">
  <a class="active">HOME</a><a>COOP PRODUCTS ▾</a><a>SPECIAL OFFER</a><a>SERVICES</a><a>ABOUT US</a><a>NEWS</a><a>FAQ</a><a>CONTACT US</a>
</nav>

<!-- hero -->
<div class="img hero" role="img" aria-label="Street scene with a bicycle and a wrapped gift, warm muted tones"></div>
<div class="abs hero-box">
  <span class="pre">WELCOME TO</span>
  <h1>UNI STORE GIFT'S</h1>
  <div class="sub">New E-Commerce Store.</div>
  <span class="btn-red">Shop Now</span>
</div>

<!-- featured -->
<div class="abs title" style="top:616px">Featured Products</div>
<span class="arrow" style="left:108px;top:760px">‹</span>
<span class="arrow" style="left:1082px;top:760px">›</span>
<div class="abs row" style="top:660px">
  <div class="card"><div class="pic" role="img" aria-label="Child holding a wrapped gift" style="background:linear-gradient(135deg,#e8c7b8,#c85a55)"></div><div class="cap">Gift Shopping</div></div>
  <div class="card"><div class="pic" role="img" aria-label="Stationery supplies on a desk" style="background:linear-gradient(135deg,#d7c3a2,#8c6c4b)"></div><div class="cap">Stationery Shopping</div></div>
  <div class="card"><div class="pic" role="img" aria-label="Computer accessories on a teal surface" style="background:linear-gradient(135deg,#8ad8d2,#5cb8b2)"></div><div class="cap">Computer Accessories</div></div>
  <div class="card"><div class="pic" role="img" aria-label="Network cables in a server rack" style="background:linear-gradient(135deg,#3b4a6b,#1b2438)"></div><div class="cap">IT Support Service</div></div>
</div>

<!-- banner -->
<div class="img banner" role="img" aria-label="Wrapped presents with red ribbons on a wooden table"></div>
<div class="abs banner-box">
  <h3>GIFTS FOR NEW ARRIVALS</h3>
  <div class="b2">PERSONALIZED GIFTS FOR YOUR HOME</div>
  <p>Made with great attention and care</p>
</div>

<!-- best sellers -->
<div class="abs title" style="top:1384px">Best Sellers</div>
<span class="arrow" style="left:108px;top:1528px">‹</span>
<span class="arrow" style="left:1082px;top:1528px">›</span>
<div class="abs row" style="top:1432px">
  <div class="card"><div class="pic" role="img" aria-label="Baby gift basket" style="height:216px;background:linear-gradient(135deg,#efd2c6,#b9574f)"></div><div class="name">Baby's Gift</div><div class="meta"><span class="stars">★★★★★</span><span>$80 - $70</span></div></div>
  <div class="card"><div class="pic" role="img" aria-label="Computer accessories on teal" style="height:216px;background:linear-gradient(135deg,#8ad8d2,#5cb8b2)"></div><div class="name">Computer Accessories</div><div class="meta"><span class="stars">★★★★★</span><span>$500 - $550</span></div></div>
  <div class="card"><div class="pic" role="img" aria-label="Laptop on a grey desk" style="height:216px;background:linear-gradient(135deg,#9a9a9a,#5a5a5a)"><span class="quick">ADD TO CART</span></div><div class="name">Laptop</div><div class="meta"><span class="stars">★★★★★</span><span>$1000 - $1500</span></div></div>
  <div class="card"><div class="pic" role="img" aria-label="Open book beside a laptop" style="height:216px;background:linear-gradient(135deg,#4b5570,#2a2f40)"></div><div class="name">All Type Book</div><div class="meta"><span class="stars">★★★★★</span><span>$80 - $120</span></div></div>
</div>

<!-- promos -->
<div class="abs promo" style="left:120px;background:linear-gradient(135deg,#e9c9b9,#c9907a)" role="img" aria-label="Stacked gift boxes in pastel paper">
  <div class="inner"><h3>New Gifts</h3><p>Fresh picks wrapped for every campus occasion</p><span class="btn-navy">Learn More</span></div>
</div>
<div class="abs promo" style="left:612px;background:linear-gradient(90deg,#1a1a1a,#3a3430)" role="img" aria-label="Wrist watch on a dark surface">
  <div class="inner"><h3>Men's Watch</h3><p>Classic styles made to last through every term</p><span class="btn-navy">Learn More</span></div>
</div>

<!-- recommended -->
<div class="abs title" style="top:2076px">Recommended for You</div>
<span class="arrow" style="left:108px;top:2224px">‹</span>
<span class="arrow" style="left:1082px;top:2224px">›</span>
<div class="abs row" style="top:2128px">
  <div class="card"><div class="pic" role="img" aria-label="Baby gift basket" style="background:linear-gradient(135deg,#efd2c6,#b9574f)"></div><div class="name">Baby's Gift</div><div class="meta"><span class="stars">★★★★★</span><span>$80 - $70</span></div></div>
  <div class="card"><div class="pic" role="img" aria-label="Shelves of books" style="background:linear-gradient(135deg,#8a6a55,#3c4a5a)"></div><div class="name">Book Accessories</div><div class="meta"><span class="stars">★★★★★</span><span>$500 - $550</span></div></div>
  <div class="card"><div class="pic" role="img" aria-label="Laptop on a grey desk" style="background:linear-gradient(135deg,#9a9a9a,#5a5a5a)"><span class="quick">ADD TO CART</span></div><div class="name">Laptop</div><div class="meta"><span class="stars">★★★★★</span><span>$1000 - $1500</span></div></div>
  <div class="card"><div class="pic" role="img" aria-label="Men's suit jacket" style="background:linear-gradient(135deg,#5d6b5e,#2c3230)"></div><div class="name">Men's Suit</div><div class="meta"><span class="stars">★★★★★</span><span>$80 - $120</span></div></div>
</div>

<!-- history -->
<section class="abs history">
  <h2>UNISTORE HISTORY</h2>
  <div class="lead">The store for our own students since its first day, built by the members.</div>
  <p>In the early years students came together to open a small shop on campus selling books, stationery and everyday goods at fair prices. Run by members for members, the store grew step by step, adding computer gear, gifts and repair help, while keeping every profit inside the student community and its clubs.</p>
  <p>Today the store serves thousands of members each term, online and in person. We keep prices low, support student projects and give back through grants, awards and campus events.</p>
  <span class="btn-outline">READ MORE STORY</span>
</section>

<!-- photofeed -->
<div class="abs feed"></div>
<svg class="abs" style="left:591px;top:2824px" width="18" height="18" viewBox="0 0 18 18"><circle cx="9" cy="9" r="8" fill="none" stroke="#2b2b2b" stroke-width="1.5"/></svg>
<div class="abs feed-title">Follow @ UNI STORE in Photofeed</div>
<div class="abs feed-row">
  <div role="img" aria-label="Store photo" style="background:#a7b6c2"></div>
  <div role="img" aria-label="Store photo" style="background:#c9a98f"></div>
  <div role="img" aria-label="Store photo" style="background:#6f7f73"></div>
  <div role="img" aria-label="Store photo" style="background:#d3c2b0"></div>
  <div role="img" aria-label="Store photo" style="background:#8a7a8f"></div>
  <div role="img" aria-label="Store photo" style="background:#b38a6c"></div>
</div>

<!-- newsletter -->
<section class="abs news">
  <h2>NEWSLETTER IN TOUCH</h2>
  <p>Subscribe right away and you will receive our latest offerings!</p>
  <div class="form"><div class="field">Enter your email address</div><div class="sub-btn">SUBSCRIBE</div></div>
</section>

<!-- footer -->
<div class="abs foot" style="left:120px"><h4>WEB LINK</h4><ul><li>Our Story</li><li>Blog</li><li>Contact Us</li><li>Terms &amp; Conditions</li><li>Privacy Policy</li><li>Payment Security</li></ul></div>
<div class="abs foot" style="left:380px"><h4>MY ACCOUNT</h4><ul><li>My Account</li><li>View Cart</li><li>Track My Order</li><li>Delivery</li></ul></div>
<div class="abs foot" style="left:632px"><h4>HELP US</h4><ul><li>Why Join?</li><li>FAQs</li><li>Shipping Policies</li><li>Returns Policy</li><li>Help Center</li></ul></div>
<div class="abs foot" style="left:888px"><h4>FOLLOW US</h4><ul><li><span class="dot"></span>Friendbook</li><li><span class="dot"></span>Chirpline</li><li><span class="dot"></span>Photofeed</li><li><span class="dot"></span>Workwire</li></ul></div>
<div class="abs copy">Copyright © Uni Store Gifts. All Rights Reserved.</div>

</body>
</html>
```